Mentor Circle Certificate - Word Template

We need a MS Word certificate template for the Storyline 9 Mentor Circle program. We are global non-profit that connects artists, educators, and students through the power of art and education. The final design should be fun and vibrant, yet professional. It shoud also include the program logo and feature the S9 purple (see brand guidelines).

Our brand guidelines are here: https://stylebookhub.example/storyline-9 and I've uploaded the program logo.

```html
<!DOCTYPE html>
<html lang="en">
<head>
<meta charset="utf-8">
<title>Storyline 9 Mentor Circle – CEU Certificate</title>
<link rel="stylesheet" href="https://fonts.googleapis.com/css2?family=Cinzel:wght@600&family=Tinos:ital,wght@0,400;0,700;1,400;1,700&family=Arimo&display=swap">
<style>
  :root {
    --page-bg: #ececec;
    --paper: #f7f7f7;
    --paper-inner: #fbfbfb;
    --guilloche-light: #e6e6e8;
    --guilloche-dark: #d3d3d6;
    --s9-purple: #5b3f99;
    --ink: #111111;
    --ink-soft: #555555;
    --rule-grey: #c4c4c8;
  }
  * { box-sizing: border-box; margin: 0; padding: 0; }
  html, body {
    width: 1200px; height: 698px; overflow: hidden;
    background: var(--page-bg);
  }
  .certificate {
    position: absolute; left: 150px; top: 24px;
    width: 900px; height: 650px;
    background: var(--paper);
    box-shadow: 0 1px 4px rgba(0,0,0,.12);
    font-family: "Tinos", "Times New Roman", serif;
    color: var(--ink);
  }
  .guilloche-field {
    position: absolute; inset: 16px;
    background: radial-gradient(ellipse at center, var(--guilloche-light) 55%, var(--guilloche-dark) 100%);
  }
  .frame-outer {
    position: absolute; left: 81px; top: 74px; width: 760px; height: 499px;
    border: 4px solid var(--s9-purple);
    background: var(--paper-inner);
  }
  .frame-mid {
    position: absolute; inset: 6px;
    border: 1.5px solid var(--s9-purple);
  }
  .frame-inner {
    position: absolute; inset: 14px;
    border: 3px solid var(--rule-grey);
  }
  .frame-core {
    position: absolute; inset: 20px;
    border: 1px solid var(--s9-purple);
    background: linear-gradient(90deg, #f4f4f4, #ffffff 50%, #f4f4f4);
  }
  .content { position: absolute; inset: 0; }
  .centered { position: absolute; left: 0; right: 0; text-align: center; }

  .program-name {
    top: 118px; font-family: "Tinos", serif; font-size: 17px;
    letter-spacing: .5px; color: var(--ink);
  }
  .title {
    top: 153px; font-family: "Cinzel", serif; font-weight: 600;
    font-size: 35px; letter-spacing: .5px; line-height: 1;
  }
  .subtitle { top: 198px; font-size: 13px; letter-spacing: .3px; }
  .ribbon { position: absolute; left: 244px; top: 222px; width: 433px; height: 22px; }
  .ribbon svg { position: absolute; inset: 0; }
  .ribbon span {
    position: absolute; inset: 0; display: flex; align-items: center; justify-content: center;
    color: #fff; font-weight: 700; font-size: 9px; letter-spacing: .3px;
  }
  .statement {
    position: absolute; left: 127px; right: 127px;
    font-size: 12.5px; white-space: nowrap;
  }
  .statement .blank {
    display: inline-block; border-bottom: 1px solid var(--ink); height: 10px; vertical-align: baseline;
  }
  .line-one { top: 268px; }
  .line-two { top: 304px; }
  .details {
    position: absolute; left: 120px; right: 120px; top: 346px;
    text-align: center; font-style: italic; font-size: 6.3px; line-height: 1.4;
    color: var(--ink-soft);
  }
  .details p { margin-bottom: 4px; }
  .details b { color: #333; }
  .certified-by { top: 462px; font-style: italic; font-weight: 700; font-size: 10px; color: #444; }
  .signature-line {
    position: absolute; left: 345px; top: 494px; width: 230px; border-top: 1px solid #444;
  }
  .signatory {
    top: 505px; font-family: "Arimo", Arial, sans-serif; font-size: 8.5px; line-height: 1.25; color: #444;
  }
</style>
</head>
<body>
<main class="certificate">
  <div class="guilloche-field" role="img" aria-label="Fine grey guilloche and rosette security pattern surrounding the certificate"></div>

  <div class="frame-outer">
    <div class="frame-mid"></div>
    <div class="frame-inner"></div>
    <div class="frame-core"></div>
  </div>

  <div class="content">
    <p class="centered program-name">Storyline 9</p>

    <h1 class="centered title">CEU CERTIFICATE</h1>
    <p class="centered subtitle">S9 MENTOR CIRCLE</p>

    <div class="ribbon">
      <svg viewBox="0 0 433 22" preserveAspectRatio="none" width="433" height="22">
        <polygon points="0,0 433,0 425,11 433,22 0,22 8,11" fill="var(--s9-purple)"/>
      </svg>
      <span>SOCIOEMOTIONAL LEARNING, NARRATIVE, LISTENING AND SPEAKING</span>
    </div>

    <p class="statement line-one">This certifies that <span class="blank" style="width:348px"></span> Participated in a series of professional</p>
    <p class="statement line-two">development experiences from &nbsp;<span class="blank" style="width:228px"></span> To <span class="blank" style="width:238px"></span>.</p>

    <div class="details">
      <p>The educator learned how to run the S9 Story Relay in live and virtual environments. The Story Relay method is designed to help students understand that their voices, stories, actions and lives matter. It is a research-proven method to foster empathy and support students' positive identity building through personal narrative.<br>
      The educator has now achieved certification as an <b>S9 Story Relay Facilitator.</b></p>
      <p>This means that they have the tools to:<br>
      Build a safe space through communication; Model and provide explicit teaching around listening; Navigate challenges in group dynamics; Manage the pair and share technique; Explain research on empathy and storytelling; Debrief about feelings, impacts, and lessons from the Story Relay experience; Address their own feelings during and after the Story Relay.</p>
      <p>In addition, the educator has done the following <b>curriculum work:</b><br>
      Conducted the Story Relay in their school; Collaborated with other teachers across the country to create curriculum connected to the Story Relay and English Language Arts standards.</p>
      <p>As a result, the individual above should receive <b>6 continuing education unit (CEUs) for 60 contact hours.</b></p>
    </div>

    <p class="centered certified-by">Certified by:</p>
    <div class="signature-line"></div>
    <p class="centered signatory">Elena Marsh<br>Director of Learning Resources<br>Storyline 9</p>
  </div>
</main>
</body>
</html>
```